Business IT Services Billboard to attract local small businesses

We are Brivolane, a premier Managed Service Provider (MSP) specializing in comprehensive IT services and VOIP phone solutions exclusively for businesses. Our goal is to create a dynamic and visually engaging billboard advertisement that not only highlights our cutting-edge IT solutions but also emphasizes our state-of-the-art VOIP phone services. This billboard should communicate our commitment to providing innovative, reliable, and holistic technology solutions.
Target Market(s)
small business
Industry/Entity Type
Information Technology
Colors
Designer to choose colors to be used in the design.
Look and feel
Each slider illustrates characteristics of the customer's brand and the style your logo design should communicate.

```html
<!DOCTYPE html>
<html lang="en">
<head>
<meta charset="utf-8">
<title>Brivolane Billboard</title>
<link href="https://fonts.googleapis.com/css2?family=Michroma&family=Poppins:wght@400;600;700&display=swap" rel="stylesheet">
<style>
  :root {
    --page-bg: #eef1f4;
    --white: #ffffff;
    --brand-blue: #0b5aa8;
    --deep-blue: #0a4d8e;
    --bright-blue: #14a2e2;
    --grey-light: #e2e2e2;
    --grey-mid: #bdbdbd;
    --grey-dark: #8f8f8f;
    --ink: #1e1e24;
    --office-light: #dfe3e8;
    --office-dark: #3e434b;
    --desk-dark: #262a31;
    --desk-warm: #7d6a58;
  }
  html, body {
    margin: 0;
    padding: 0;
    width: 1200px;
    height: 1117px;
    overflow: hidden;
    background: var(--page-bg);
  }
  .billboard {
    position: absolute;
    left: 0;
    top: 252px;
    width: 1200px;
    height: 612px;
    display: block;
  }
  .logo-name { font-family: "Michroma", sans-serif; fill: var(--brand-blue); }
  .headline { font-family: "Michroma", sans-serif; fill: var(--white); font-weight: 700; }
  .tagline { font-family: "Poppins", sans-serif; font-weight: 700; fill: var(--white); }
  .intro { font-family: "Poppins", sans-serif; font-weight: 400; fill: var(--ink); }
  .cta-lead { font-family: "Michroma", sans-serif; fill: var(--white); }
  .cta-url { font-family: "Michroma", sans-serif; fill: var(--white); font-weight: 700; }
</style>
</head>
<body>
<svg class="billboard" viewBox="0 0 1200 612" xmlns="http://www.w3.org/2000/svg">
  <defs>
    <clipPath id="board-clip"><rect width="1200" height="612"/></clipPath>
    <linearGradient id="headline-band" x1="0" y1="0" x2="1" y2="0.3">
      <stop offset="0" stop-color="var(--brand-blue)"/>
      <stop offset="0.55" stop-color="#0d7cc6"/>
      <stop offset="1" stop-color="var(--bright-blue)"/>
    </linearGradient>
    <linearGradient id="intro-band" x1="0" y1="0" x2="1" y2="0">
      <stop offset="0" stop-color="var(--grey-mid)"/>
      <stop offset="0.5" stop-color="var(--grey-light)"/>
      <stop offset="1" stop-color="var(--grey-dark)"/>
    </linearGradient>
    <linearGradient id="office-photo" x1="0" y1="0" x2="0.6" y2="1">
      <stop offset="0" stop-color="var(--office-light)"/>
      <stop offset="0.5" stop-color="#9aa0a8"/>
      <stop offset="1" stop-color="var(--office-dark)"/>
    </linearGradient>
    <linearGradient id="desk-photo" x1="0" y1="0" x2="0" y2="1">
      <stop offset="0" stop-color="#4a5carry"/>
      <stop offset="0" stop-color="#51606e"/>
      <stop offset="0.55" stop-color="var(--desk-dark)"/>
      <stop offset="1" stop-color="var(--desk-warm)"/>
    </linearGradient>
    <linearGradient id="url-pill" x1="0" y1="0" x2="0" y2="1">
      <stop offset="0" stop-color="#1a86d4"/>
      <stop offset="1" stop-color="var(--brand-blue)"/>
    </linearGradient>
  </defs>

  <g clip-path="url(#board-clip)">
    <!-- header band -->
    <rect class="header-band" x="0" y="0" width="1200" height="129" fill="var(--white)"/>
    <text class="logo-name" x="63" y="99" font-size="64" textLength="674" lengthAdjust="spacingAndGlyphs">BRIVOLANE</text>

    <!-- headline band -->
    <rect class="headline-band" x="0" y="129" width="1200" height="205" fill="url(#headline-band)"/>
    <line x1="0" y1="147" x2="735" y2="147" stroke="var(--deep-blue)" stroke-width="2"/>
    <text class="headline" font-size="30">
      <tspan x="63" y="203" textLength="566" lengthAdjust="spacingAndGlyphs">ELEVATE YOUR BUSINESS</tspan>
      <tspan x="63" y="237" textLength="515" lengthAdjust="spacingAndGlyphs">WITH NEXT-GEN IT AND</tspan>
      <tspan x="63" y="271" textLength="615" lengthAdjust="spacingAndGlyphs">VOIP SERVICES INNOVATIVE</tspan>
    </text>
    <text class="tagline" x="62" y="311" font-size="19" textLength="600" lengthAdjust="spacingAndGlyphs">IT and VOIP Solutions Tailored for Your Business Success.</text>

    <!-- intro band -->
    <rect class="intro-band" x="0" y="339" width="1200" height="97" fill="url(#intro-band)"/>
    <line x1="0" y1="337" x2="760" y2="337" stroke="var(--white)" stroke-width="4"/>
    <text class="intro" font-size="17">
      <tspan x="66" y="376" textLength="564" lengthAdjust="spacingAndGlyphs">We are Brivolane, a premier Managed Service Provider (MSP)</tspan>
      <tspan x="66" y="396" textLength="516" lengthAdjust="spacingAndGlyphs">specializing in comprehensive IT services and VOIP phone</tspan>
      <tspan x="66" y="416" textLength="322" lengthAdjust="spacingAndGlyphs">solutions exclusively for businesses.</tspan>
    </text>

    <!-- call to action band -->
    <rect class="cta-band" x="0" y="436" width="1200" height="176" fill="var(--deep-blue)"/>
    <text class="cta-lead" x="326" y="481" font-size="19" text-anchor="middle" textLength="404" lengthAdjust="spacingAndGlyphs">Transform Your Tech Today at</text>
    <rect x="72" y="500" width="512" height="77" rx="38" fill="#111"/>
    <rect x="69" y="496" width="512" height="76" rx="38" fill="var(--grey-mid)" stroke="var(--white)" stroke-width="3"/>
    <rect x="78" y="504" width="494" height="60" rx="30" fill="url(#url-pill)"/>
    <text class="cta-url" x="325" y="546" font-size="28" text-anchor="middle" textLength="446" lengthAdjust="spacingAndGlyphs">www.brivolane.com.</text>

    <!-- main photo area -->
    <path d="M885 0 Q760 140 748 340 L748 612 L1200 612 L1200 0 Z" fill="var(--brand-blue)"/>
    <path d="M855 0 Q765 80 735 210" fill="none" stroke="var(--white)" stroke-width="4"/>
    <path d="M800 240 L800 300" fill="none" stroke="var(--white)" stroke-width="3"/>
    <path class="office-photo" role="img" aria-label="Photo: two smiling business colleagues in suits reviewing a tablet in a bright office" d="M890 0 L1200 0 L1200 612 L765 612 L765 330 Q775 140 890 0 Z" fill="url(#office-photo)"/>

    <!-- desk phone circle -->
    <circle cx="780" cy="470" r="184" fill="var(--brand-blue)"/>
    <circle cx="780" cy="470" r="172" fill="var(--white)"/>
    <circle class="desk-photo" role="img" aria-label="Photo: office VOIP desk phone with headset on a wooden desk" cx="780" cy="470" r="165" fill="url(#desk-photo)"/>
  </g>
</svg>
</body>
</html>
```